BOOK COVER for THE IRONCLAD VENTURIST

I am publishing my first book and need to nail the cover. The cover should feature my picture as this is a major branding play.
TITLE: The Ironclad Venturist.
SUBTITLE: Forging A Lasting Company Heritage.
BOOK DESCRIPTION: "The Ironclad Venturist," presents a comprehensive approach to building resilient and sustainable businesses. The book emphasizes the inevitability of challenges in the business world and stresses the importance of resilience in facing adversity. It highlights the concept of "Shatterproofing" a business, drawing inspiration from the safety glass used in car windshields, which doesn't shatter upon impact​​.

The book identifies two primary types of business owners: "CAPTIVES," who are overwhelmed and cannot take a break from their businesses without facing chaos, and "SHATTERPROOF" entrepreneurs, who have established systems and processes, clear goals, and can step away from their businesses without encountering problems​​. It raises critical questions about why some business owners become "CAPTIVES" while others achieve a "SHATTERPROOF" state and explores the transition from one to the other​​.

Dulwa points out that many well-intentioned business founders often lack a comprehensive roadmap or blueprint, leading to vulnerabilities in their businesses​​. Reflecting on his own journey from being a "CAPTIVE" to becoming "SHATTERPROOF," Dulwa shares insights from his experiences and the lessons he learned along the way​​.

The book addresses the legal aspects of businesses, an often overlooked area in entrepreneurial literature, providing readers with a roadmap and the necessary legal systems and structures to build a "SHATTERPROOF" business​​. This approach led to the development of Dulwa's Beacon Counsel Mentoring Membership and the Ironclad Method​​.

Dulwa encourages business owners to shift their paradigm, viewing lawyers as primary care providers for their businesses rather than turning to them only in emergencies​​. "The Ironclad Venturist" is an invitation to make this paradigm shift and provides a roadmap for becoming a resilient and successful entrepreneur​​.

Target Market(s)

Small business owners from Start-up to $10 Million

Industry/Entity Type

Legal / Entrepreneurship

Font styles to use
Serif

Colors
0054AA
0677BA
7BADD7
CADEEF
E8F1F8

Requirements
Must have
• I am publishing my first book and need to nail the cover. The cover should feature my picture as this is a major branding play. The foreward has been written by Ned Pomfrey. This needs to be included in the cover.

```html
<!DOCTYPE html>
<html lang="en">
<head>
<meta charset="utf-8">
<title>The Ironclad Venturist — Book Cover</title>
<link rel="stylesheet" href="https://fonts.googleapis.com/css2?family=Bebas+Neue&family=Poppins:wght@400;500&display=swap">
<style>
  :root {
    --backdrop: #c4c5c7;
    --navy: #1b2a63;
    --title-white: #ffffff;
    --title-red: #d21f26;
    --subtitle-cyan: #3fc4e6;
    --photo-brown: #6b4a33;
    --photo-dark: #1a1a1c;
    --photo-suit: #26408a;
    --photo-suit-deep: #1a2b66;
    --photo-shirt: #c9d3e6;
  }
  * { margin: 0; padding: 0; box-sizing: border-box; }
  html, body {
    width: 1129px;
    height: 1200px;
    overflow: hidden;
    background: var(--backdrop);
  }
  .canvas {
    position: relative;
    width: 1129px;
    height: 1200px;
  }
  .cover {
    position: absolute;
    left: 185px;
    top: 30px;
    width: 760px;
    height: 1140px;
    overflow: hidden;
    background: var(--photo-dark);
  }
  .cover-backdrop {
    position: absolute;
    inset: 0;
    background:
      radial-gradient(ellipse 60% 45% at 85% 70%, #3b3b3e 0%, rgba(59,59,62,0) 100%),
      linear-gradient(115deg, var(--photo-brown) 0%, #4a3526 30%, #262220 55%, var(--photo-dark) 80%);
  }
  .author-photo {
    position: absolute;
    left: 50px;
    top: 470px;
    width: 530px;
    height: 620px;
    border-radius: 200px 200px 0 0;
    background:
      linear-gradient(90deg, rgba(201,211,230,0) 40%, rgba(201,211,230,0.55) 48%, rgba(201,211,230,0.55) 54%, rgba(201,211,230,0) 62%),
      linear-gradient(180deg, var(--photo-suit) 0%, var(--photo-suit-deep) 100%);
  }
  .title {
    position: absolute;
    top: 34px;
    left: 40px;
    right: 36px;
    font-family: "Bebas Neue", "Arial Narrow", sans-serif;
    font-weight: 400;
    line-height: 0.86;
    text-align: right;
  }
  .title-line {
    display: block;
    font-size: 150px;
    letter-spacing: 1px;
  }
  .title-line--white { color: var(--title-white); }
  .title-line--red { color: var(--title-red); }
  .subtitle {
    position: absolute;
    top: 330px;
    right: 60px;
    width: 300px;
    font-family: "Poppins", sans-serif;
    font-weight: 400;
    font-size: 34px;
    line-height: 1.05;
    color: var(--subtitle-cyan);
  }
  .author-band {
    position: absolute;
    left: 0;
    bottom: 0;
    width: 760px;
    height: 360px;
  }
  .author-name {
    position: absolute;
    left: 70px;
    bottom: 150px;
    font-family: "Poppins", sans-serif;
    font-weight: 400;
    font-size: 36px;
    letter-spacing: 1px;
    color: var(--title-white);
  }
  .foreword-credit {
    position: absolute;
    left: 70px;
    bottom: 95px;
    font-family: "Poppins", sans-serif;
    font-weight: 400;
    font-size: 22px;
    letter-spacing: 0.5px;
    color: var(--subtitle-cyan);
  }
</style>
</head>
<body>
  <div class="canvas">
    <section class="cover">
      <div class="cover-backdrop"></div>
      <div class="author-photo" role="img" aria-label="Photograph of the author seated in a navy suit and light shirt, adjusting his cuff, in a warm-toned office"></div>

      <h1 class="title">
        <span class="title-line title-line--white">The Ironclad</span>
        <span class="title-line title-line--red">Venturist</span>
      </h1>

      <p class="subtitle">Forging A Lasting Company Heritage</p>

      <svg class="author-band" viewBox="0 0 760 360" aria-hidden="true">
        <path d="M0 40 L40 46 L70 44 L110 60 L150 62 L190 80 L230 86 L270 102 L310 110 L350 126 L390 134 L430 150 L470 160 L510 176 L550 186 L590 204 L630 212 L670 230 L710 240 L760 258 L760 360 L0 360 Z"
              fill="#f2f2f2"/>
        <path d="M0 48 L40 54 L70 52 L110 68 L150 70 L190 88 L230 94 L270 110 L310 118 L350 134 L390 142 L430 158 L470 168 L510 184 L550 194 L590 212 L630 220 L670 238 L710 248 L760 266 L760 360 L0 360 Z"
              fill="var(--navy)"/>
      </svg>

      <p class="author-name">SCOTT DULWA</p>
      <p class="foreword-credit">Foreword by Ned Pomfrey</p>
    </section>
  </div>
</body>
</html>
```